Package for Utensil Kit

we want to have a new design for our utensil kit, its a paper bag with both sides like files below. our website is www.peckbox.com and please use #FF6C0E as the main color and feel free to unleash your creativity.
the deadcut of the package is 14x26cm.pdf also showed the size.
in the front we want to show our band
in the back we need info list here:
1. www.peckbox.com and QR code
2.our locations (Now four) and phone number
3.other information needed

```html
<!DOCTYPE html>
<html lang="en">
<head>
<meta charset="utf-8">
<title>PeckBox Utensil Kit – Dieline</title>
<link href="https://fonts.googleapis.com/css2?family=Oswald:wght@400;500;700&display=swap" rel="stylesheet">
<style>
  :root {
    --brand: #FF6C0E;
    --brand-deep: #FA4E0A;
    --paper: #FFFFFF;
    --guide: #39E639;
    --ink: #111111;
    --stage: #FFFFFF;
  }
  * { box-sizing: border-box; margin: 0; padding: 0; }
  html, body { width: 1200px; height: 713px; overflow: hidden; background: var(--stage); }
  body { position: relative; font-family: "Oswald", sans-serif; }

  .measure { position: absolute; font-size: 11px; color: var(--ink); text-align: center; }
  .measure--top { top: 40px; }
  .measure--side { left: 772px; top: 360px; transform: rotate(90deg); transform-origin: left top; }

  .dieline {
    position: absolute; left: 432px; top: 60px;
    width: 336px; height: 624px;
    background: var(--brand-deep); overflow: hidden;
  }
  .dieline__layer { position: absolute; inset: 0; }
  .guide-v { position: absolute; top: 0; bottom: 0; width: 1px; background: var(--guide); }
  .guide-h { position: absolute; left: 0; right: 0; border-top: 1px dashed var(--guide); }
  .guide-h--bottom { border-top-color: #9A9A9A; }
  .crop-mark { position: absolute; bottom: 0; width: 24px; height: 12px; background: var(--ink); }

  .qr-slot { position: absolute; left: 245px; top: 58px; width: 62px; height: 62px; background: var(--paper); border-radius: 8px; }

  .rot { position: absolute; transform-origin: center; white-space: nowrap; }
  .rot--cw { transform: rotate(90deg); }
  .rot--ccw { transform: rotate(-90deg); }

  .brand-name {
    left: 47px; top: 115px; width: 246px; height: 70px;
    color: var(--paper); font-weight: 700; font-size: 62px; line-height: 70px; text-align: center;
  }
  .brand-tagline {
    left: 72px; top: 86px; width: 130px; height: 14px;
    color: var(--paper); font-weight: 500; font-size: 13px; line-height: 14px; letter-spacing: .8px;
  }
  .web-address {
    left: 197px; top: 209px; width: 160px; height: 18px;
    color: var(--paper); font-weight: 700; font-size: 15.5px; line-height: 18px; text-align: center;
  }

  .locations {
    left: -78px; top: 384px; width: 279px; height: 63px;
    color: var(--brand-deep); display: flex; flex-direction: column; gap: 5px;
  }
  .locations__heading { display: flex; align-items: center; gap: 5px; font-size: 8px; font-weight: 500; }
  .locations__heading::after { content: ""; flex: 1; height: 1.5px; background: var(--brand-deep); }
  .locations__grid { display: grid; grid-template-columns: 1fr 1fr; gap: 4px 10px; }
  .store__name { font-size: 8.5px; font-weight: 500; line-height: 10px; }
  .store__detail { font-size: 5px; line-height: 6px; color: var(--ink); }
</style>
</head>
<body>
  <div class="measure measure--top" style="left:432px;width:24px">1cm</div>
  <div class="measure measure--top" style="left:456px;width:72px">3cm</div>
  <div class="measure measure--top" style="left:528px;width:144px">6cm</div>
  <div class="measure measure--top" style="left:672px;width:72px">3cm</div>
  <div class="measure measure--top" style="left:744px;width:24px">1cm</div>
  <div class="measure measure--side">26cm</div>

  <div class="dieline">
    <svg class="dieline__layer" viewBox="0 0 336 624" width="336" height="624">
      <defs>
        <radialGradient id="tint-on-white" cx="50%" cy="45%" r="60%">
          <stop offset="0" stop-color="#FFC7A3"/>
          <stop offset="0.7" stop-color="#FFDCC6"/>
          <stop offset="1" stop-color="#FFEFE4"/>
        </radialGradient>
        <radialGradient id="tint-on-brand" cx="50%" cy="45%" r="60%">
          <stop offset="0" stop-color="#FFA56E"/>
          <stop offset="1" stop-color="#FF7A35"/>
        </radialGradient>
      </defs>
      <path d="M0 221 C 95 206, 262 330, 264 624 L0 624 Z" fill="var(--paper)"/>

      <g role="img" aria-label="Line sketch of a bunch of carrots">
        <ellipse cx="57" cy="91" rx="18" ry="40" transform="rotate(-35 57 91)" fill="url(#tint-on-brand)"/>
      </g>
      <g role="img" aria-label="Line sketch of a tomato">
        <circle cx="58" cy="176" r="28" fill="url(#tint-on-brand)"/>
      </g>
      <g role="img" aria-label="Line sketch of a sliced tomato">
        <ellipse cx="210" cy="288" rx="24" ry="21" fill="url(#tint-on-brand)"/>
      </g>
      <g role="img" aria-label="Line sketch of a tomato">
        <ellipse cx="281" cy="373" rx="24" ry="22" fill="url(#tint-on-brand)"/>
      </g>
      <g role="img" aria-label="Line sketch of sliced cucumber rounds">
        <ellipse cx="120" cy="297" rx="20" ry="21" fill="url(#tint-on-white)"/>
      </g>
      <g role="img" aria-label="Line sketch of a whole roast chicken">
        <ellipse cx="168" cy="428" rx="58" ry="112" transform="rotate(-18 168 428)" fill="url(#tint-on-white)"/>
      </g>
      <g role="img" aria-label="Line sketch of a garlic bulb and clove">
        <ellipse cx="140" cy="560" rx="38" ry="30" fill="url(#tint-on-white)"/>
      </g>
    </svg>

    <div class="qr-slot"></div>

    <div class="rot rot--cw brand-name">PeckBox</div>
    <div class="rot rot--cw brand-tagline">HAINAN CHICKEN</div>
    <div class="rot rot--cw web-address">www.peckbox.com</div>

    <div class="rot rot--ccw locations">
      <div class="locations__heading">OUR LOCATION</div>
      <div class="locations__grid">
        <div class="store">
          <div class="store__name">PeckBox - Alder Heights</div>
          <div class="store__detail">18 Maple Ave. - Alder Heights, CA 90001</div>
          <div class="store__detail">(626) 555-0101</div>
        </div>
        <div class="store">
          <div class="store__name">PeckBox - West Linden</div>
          <div class="store__detail">240 Cedar Blvd. - West Linden, CA 90002</div>
          <div class="store__detail">(626) 555-0102</div>
        </div>
        <div class="store">
          <div class="store__name">PeckBox - Pinecrest</div>
          <div class="store__detail">77 Oak St. - Pinecrest, CA 90003</div>
          <div class="store__detail">(626) 555-0103</div>
        </div>
        <div class="store">
          <div class="store__name">PeckBox - Briarwood</div>
          <div class="store__detail">95 Birch Rd. - Briarwood, CA 90004</div>
          <div class="store__detail">(626) 555-0104</div>
        </div>
      </div>
    </div>

    <div class="guide-v" style="left:0"></div>
    <div class="guide-v" style="left:24px"></div>
    <div class="guide-v" style="left:96px"></div>
    <div class="guide-v" style="left:240px"></div>
    <div class="guide-v" style="left:312px"></div>
    <div class="guide-v" style="left:335px"></div>
    <div class="guide-h" style="top:0;border-top-style:solid"></div>
    <div class="guide-h" style="top:24px"></div>
    <div class="guide-h guide-h--bottom" style="top:600px"></div>
    <div class="crop-mark" style="left:0"></div>
    <div class="crop-mark" style="right:0"></div>
  </div>
</body>
</html>
```